Wombella Extra Virgin Olive Oil

We need a label design for a funky Australian Extra Virgin olive oil which will target exclusively female customers that wish to utilise the product for health and beauty. We need it to have a fun and sexy modern design and it must feature an image either photo/animation/abstract or caricature of a healthy young woman. The image must be able to be used royalty free. The Olive Oil is called WOMBELLA.

The label is for a 250ml bottle. The label size is 154mm high x 50mm Wide

I have attached the type of bottle and a couple of images just to point in the right direction.

```html
<!DOCTYPE html>
<html lang="en">
<head>
<meta charset="utf-8">
<title>Wombella Extra Virgin Olive Oil – Label</title>
<link rel="stylesheet" href="https://fonts.googleapis.com/css2?family=Tinos:wght@400&display=swap">
<style>
  :root {
    --page: #ffffff;
    --label-black: #0b0b0b;
    --photo-yellow: #c9c41c;
    --photo-olive: #9a9a12;
    --photo-red: #b0231f;
    --swoosh-white: #f2f2f2;
    --swoosh-grey: #8a8a8a;
    --tree-grey: #3a3a3a;
    --title-white: #ffffff;
    --volume-yellow: #d9cf1e;
    --volume-text: #1a1a1a;
  }
  * { box-sizing: border-box; margin: 0; padding: 0; }
  html, body {
    width: 803px; height: 1200px;
    overflow: hidden;
    background: var(--page);
  }
  .canvas {
    position: relative;
    width: 803px; height: 1200px;
  }
  .label {
    position: absolute;
    left: 231px; top: 30px;
    width: 340px; height: 1140px;
    background: var(--label-black);
    overflow: hidden;
  }
  .label__photo {
    position: absolute;
    left: 0; top: 0;
    width: 340px; height: 420px;
    background:
      radial-gradient(ellipse 55% 45% at 30% 30%, #b98a5e 0%, rgba(185,138,94,0) 70%),
      radial-gradient(ellipse 60% 50% at 25% 85%, var(--photo-red) 0%, rgba(176,35,31,0) 75%),
      linear-gradient(160deg, var(--photo-olive) 0%, var(--photo-yellow) 45%, var(--photo-yellow) 70%, #d8a51c 100%);
  }
  .label__swoosh {
    position: absolute;
    left: 0; top: 360px;
    width: 340px; height: 80px;
  }
  .label__tree {
    position: absolute;
    left: 0; top: 545px;
    width: 340px; height: 595px;
    background: radial-gradient(ellipse 55% 60% at 50% 35%, var(--tree-grey) 0%, rgba(58,58,58,0.35) 45%, rgba(11,11,11,0) 80%);
  }
  .brand {
    position: absolute;
    left: 0; top: 500px;
    width: 340px;
    text-align: center;
    font-family: "Tinos", "Times New Roman", serif;
    font-weight: 400;
    font-size: 54px;
    line-height: 64px;
    color: var(--title-white);
  }
  .product-title {
    position: absolute;
    left: 0; top: 680px;
    width: 340px;
    text-align: center;
    font-family: "Tinos", "Times New Roman", serif;
    font-weight: 400;
    font-size: 43px;
    line-height: 59px;
    color: var(--title-white);
  }
  .volume {
    position: absolute;
    left: 38px; top: 1078px;
    width: 268px; height: 50px;
    border-radius: 8px;
    background: var(--volume-yellow);
    text-align: center;
    font-family: "Tinos", "Times New Roman", serif;
    font-size: 19px;
    line-height: 22px;
    color: var(--volume-text);
    padding-top: 3px;
  }
</style>
</head>
<body>
  <main class="canvas">
    <section class="label">
      <div class="label__photo" role="img" aria-label="Photograph of a smiling young woman with long hair in a red top and yellow shirt against a yellow background"></div>

      <svg class="label__swoosh" viewBox="0 0 340 80" aria-hidden="true">
        <path d="M0 58 C 90 60, 200 10, 340 8 L 340 80 L 0 80 Z" fill="var(--label-black)"/>
        <path d="M0 50 C 90 52, 200 4, 340 0 L 340 8 C 200 14, 90 62, 0 62 Z" fill="var(--swoosh-white)"/>
        <path d="M0 62 C 90 62, 200 14, 340 8 L 340 14 C 200 22, 90 70, 0 70 Z" fill="var(--swoosh-grey)"/>
      </svg>

      <div class="label__tree" role="img" aria-label="Faint grey silhouette of an olive tree"></div>

      <p class="brand">Wombella</p>

      <h1 class="product-title">EXTRA<br>VIRGEN<br>OLIVE<br>OIL</h1>

      <p class="volume">250ml 8.5 fl oz<br>Australian product</p>
    </section>
  </main>
</body>
</html>
```